A new company focused on starting and investing in transformative businesses.

We need a simple and clean website with a few pages. we like larkmeadow.com as a starting point. we want the landing page to be very simple with an option to click through on the top right into INVESTOR LOGIN. then we want to be able to scroll down to see more about our company.

Target Market(s)

professional

Coding

Coded - Design and coding required

Number of Pages Required

2 page

Font styles to use
Serif
Sans Serif

Requirements
Must have
• HALVERN BUILDERS logo (attached as a file) on the top with INVESTOR LOGIN as a click through on the right. Please model the click through from larkmeadow.com. The description (also written in attached file) should be on the landing page. we do not want to have to scroll to read the description.

Then we can scroll down to read more about Halvern including the mission and the two types of businesses. More is detailed on the attached file called "Halvern Website Syntax"
Should not have
• should not be slow loading with lots of fancy graphics. should not be busy and with too many colors.

```html
<!DOCTYPE html>
<html lang="en">
<head>
<meta charset="utf-8">
<title>Halvern Builders</title>
<link href="https://fonts.googleapis.com/css2?family=Figtree:wght@400;500;600;800&family=Open+Sans:wght@400&display=swap" rel="stylesheet">
<style>
  :root {
    --blue-deep: #0a3f86;
    --blue-mid: #0f5aa8;
    --blue-brand: #0b5aa2;
    --white: #ffffff;
    --ink-soft: #5f5f5f;
    --footer-bg: #231f20;
    --footer-rule: #4a4647;
    --accent-strip: #0d5cab;
  }
  * { box-sizing: border-box; margin: 0; padding: 0; }
  html, body { width: 1200px; height: 1138px; overflow: hidden; }
  body { font-family: "Figtree", sans-serif; background: var(--white); position: relative; }

  .hero { position: absolute; left: 0; top: 0; width: 1200px; height: 592px; overflow: hidden; }
  .hero-photo {
    position: absolute; inset: 0;
    background: linear-gradient(100deg, #0c56a6 0%, #0b4c98 45%, #0a3f80 75%, #093872 100%);
  }
  .site-header { position: absolute; left: 194px; right: 194px; top: 24px; height: 48px; display: flex; justify-content: space-between; align-items: center; }
  .brand { color: var(--white); font-weight: 600; font-size: 19px; letter-spacing: 0.5px; display: flex; align-items: center; gap: 10px; }
  .brand-square { width: 30px; height: 30px; background: var(--white); }
  .investor-login { color: var(--white); font-weight: 500; font-size: 14px; text-decoration: none; display: flex; align-items: center; gap: 8px; margin-top: -6px; }
  .hero-title {
    position: absolute; left: 0; right: 0; top: 226px; text-align: center;
    color: var(--white); font-weight: 500; font-size: 33px; line-height: 42px;
  }
  .hero-title strong { font-weight: 800; }
  .scroll-cue { position: absolute; left: 589px; top: 428px; }

  .about { position: absolute; left: 0; top: 592px; width: 1200px; height: 354px; }
  .mission {
    position: absolute; left: 194px; top: 86px; width: 360px; height: 151px;
    border-left: 6px solid var(--blue-brand); padding: 6px 0 0 19px;
    font-family: "Open Sans", sans-serif; font-size: 21px; line-height: 29px; color: var(--blue-brand); letter-spacing: 0.3px;
  }
  .divider { position: absolute; left: 595px; top: 93px; width: 1px; height: 151px; background: #333; }
  .divider-arrow { position: absolute; left: 596px; top: 160px; }
  .focus-areas { position: absolute; left: 661px; top: 62px; width: 345px; }
  .focus-title { font-weight: 800; font-size: 25px; color: var(--blue-brand); line-height: 30px; margin-bottom: 6px; }
  .focus-text { font-family: "Open Sans", sans-serif; font-size: 12.3px; line-height: 18.4px; color: var(--ink-soft); margin-bottom: 12px; }

  .site-footer { position: absolute; left: 0; top: 946px; width: 1200px; height: 187px; background: var(--footer-bg); color: var(--white); text-align: center; }
  .footer-name { font-weight: 800; font-size: 25px; margin-top: 44px; line-height: 30px; }
  .footer-contact { font-size: 13px; margin-top: 3px; }
  .footer-rule { width: 812px; height: 1px; background: var(--footer-rule); margin: 18px auto 0; }
  .footer-copy { font-size: 10px; font-weight: 500; margin-top: 16px; }
  .accent-strip { position: absolute; left: 0; top: 1133px; width: 1200px; height: 5px; background: var(--accent-strip); }
</style>
</head>
<body>
  <section class="hero">
    <div class="hero-photo" role="img" aria-label="Blue-toned photo of business people meeting in an office in front of a rising chart"></div>
    <header class="site-header">
      <div class="brand"><span class="brand-square"></span>HALVERN BUILDERS</div>
      <a class="investor-login" href="#">
        <svg width="15" height="13" viewBox="0 0 15 13"><path d="M0 5h6V2l5 4.5L6 11V8H0z" fill="#fff"/><path d="M9 0h4a2 2 0 0 1 2 2v9a2 2 0 0 1-2 2H9v-2h4V2H9z" fill="#fff"/></svg>
        Investor Login
      </a>
    </header>
    <h1 class="hero-title"><strong>Halvern Builders</strong> is an entrepreneurial<br>firm focused on building and growing<br>transformational companies</h1>
    <svg class="scroll-cue" width="22" height="33" viewBox="0 0 22 33"><rect x="1.5" y="1.5" width="19" height="30" rx="9.5" fill="none" stroke="#fff" stroke-width="2.2"/><line x1="11" y1="7" x2="11" y2="13" stroke="#fff" stroke-width="2.2" stroke-linecap="round"/></svg>
  </section>

  <section class="about">
    <p class="mission">Our mission is to build meaningful businesses that create enduring value by impacting people in a measurable way.</p>
    <div class="divider"></div>
    <svg class="divider-arrow" width="10" height="16" viewBox="0 0 10 16"><path d="M0 0l10 8-10 8z" fill="var(--blue-brand)"/></svg>
    <div class="focus-areas">
      <h2 class="focus-title">Ground Up</h2>
      <p class="focus-text">Our ground up business applies a proven analytic process to identify value edge, a form of competitive advantage. We architect transformational companies and are deliberate in creating the foundation necessary to lead an industry.</p>
      <h2 class="focus-title">Special Opportunities</h2>
      <p class="focus-text">We partner with exceptional teams that create value by transforming lives. Our investment focus includes large companies and spin-outs.</p>
    </div>
  </section>

  <footer class="site-footer">
    <div class="footer-name">Halvern Builders</div>
    <p class="footer-contact">For media inquiries, please contact press@halvernbuilders.com</p>
    <div class="footer-rule"></div>
    <p class="footer-copy">© Halvern Builders 2021. All Rights Reserved.</p>
  </footer>
  <div class="accent-strip"></div>
</body>
</html>
```